Manufacturing company needs new business card.

I need a unique Business Card that will truly stand out. Nothing too busy. Simple is good, right? Not looking for a standard design either. No cookie cutter layout. I am just looking for something interesting and a bit different. Does't have to completely off the wall crazy, just not your run of the mill business card. Clean and modern with a touch of industrial.

Target Market(s)

Air conditioning industry, Architects, builders.

Industry/Entity Type

Business

Contact Information for Business Card

Details to be included on card are:

Peter Vance
Managing Director

T: 1300 847 519
M: 0428 593 174
W: www.brenvaleworks.com.au
E: peter.vance@brenvaleworks.com.au
A: 58 Harwick Lane, Sydney NSW 2000

Font styles to use
Sans Serif

Colors
0355a3
848484
fbfbfb

Requirements
Must have
• Card design must be landscape.

```html
<!DOCTYPE html>
<html lang="en">
<head>
<meta charset="utf-8">
<title>Brenvale Works – Business Card</title>
<link rel="stylesheet" href="https://fonts.googleapis.com/css2?family=Roboto:wght@400;500;700&display=swap">
<style>
  :root {
    --brand-blue: #0355a3;
    --navy: #0d2a73;
    --steel-grey: #848484;
    --paper: #fbfbfb;
    --card-black: #0b0b0b;
    --stage: #3a3a3a;
    --ink: #0d2a73;
  }
  * { margin: 0; padding: 0; box-sizing: border-box; }
  html, body {
    width: 1200px; height: 873px; overflow: hidden;
    background: var(--stage);
    font-family: "Roboto", Arial, sans-serif;
  }
  .stage {
    position: relative; width: 1200px; height: 873px;
  }
  .card {
    position: absolute; left: 320px; width: 560px; height: 320px;
    border-radius: 3px; overflow: hidden;
    box-shadow: 0 10px 30px rgba(0,0,0,.45);
  }
  .card-back { top: 76px; background: var(--card-black); }
  .card-front { top: 476px; background: var(--paper); }

  .wordmark {
    position: absolute; display: flex; align-items: center; gap: 12px;
    font-weight: 500; letter-spacing: .2px; white-space: nowrap;
  }
  .wordmark .mark { display: block; }
  .card-back .wordmark {
    left: 50%; top: 50%; transform: translate(-50%, -50%);
    color: #e6e6e6; font-size: 30px;
  }
  .card-back .wordmark .mark { width: 26px; height: 26px; background: #e6e6e6; }
  .card-front .wordmark {
    left: 72px; top: 66px; color: var(--brand-blue); font-size: 30px;
  }
  .card-front .wordmark .mark { width: 30px; height: 30px; background: var(--brand-blue); }

  .wave { position: absolute; inset: 0; }

  .holder {
    position: absolute; right: 40px; top: 100px; text-align: right; color: var(--ink);
  }
  .holder-name { font-size: 16px; font-weight: 700; }
  .holder-role { font-size: 12.5px; color: var(--brand-blue); margin-top: 1px; }

  .contacts {
    position: absolute; left: 26px; top: 226px; list-style: none;
    color: #ffffff; font-size: 13px; line-height: 17px;
  }
  .contacts li { display: flex; align-items: center; gap: 10px; }
  .contacts svg { width: 10px; height: 10px; fill: #c9cfe0; flex: none; }
</style>
</head>
<body>
<main class="stage">

  <section class="card card-back" aria-label="Business card, back">
    <div class="wordmark"><span class="mark"></span>Brenvale Works</div>
  </section>

  <section class="card card-front" aria-label="Business card, front">
    <svg class="wave" viewBox="0 0 560 320" preserveAspectRatio="none" aria-hidden="true">
      <path d="M0 196 C 190 170, 380 192, 560 96 L560 112 C 380 206, 190 184, 0 210 Z" fill="var(--steel-grey)"/>
      <path d="M0 215 C 200 190, 380 212, 560 120 L560 320 L0 320 Z" fill="var(--navy)"/>
    </svg>

    <div class="wordmark"><span class="mark"></span>Brenvale Works</div>

    <div class="holder">
      <p class="holder-name">Peter Vance</p>
      <p class="holder-role">Managing Director</p>
    </div>

    <ul class="contacts">
      <li><svg viewBox="0 0 10 10"><path d="M1 3 Q5 0 9 3 L8 4.5 L6.5 3.8 L6.5 3 Q5 2.6 3.5 3 L3.5 3.8 L2 4.5 Z M2 5 H8 V9 H2 Z"/></svg>1300 847 519</li>
      <li><svg viewBox="0 0 10 10"><rect x="3" y="0.5" width="4.5" height="9" rx="1"/></svg>0428 593 174</li>
      <li><svg viewBox="0 0 10 10"><path d="M1 9 L4 6 L5 7 L2 10 Z M5 3 L8 0 L10 2 L7 5 L6 4 L8 2 L7 1 Z M3 7 L7 3 L7.6 3.6 L3.6 7.6 Z"/></svg>www.brenvaleworks.com.au</li>
      <li><svg viewBox="0 0 10 10"><path d="M0 2 H10 V8 H0 Z"/></svg>peter.vance@brenvaleworks.com.au</li>
      <li><svg viewBox="0 0 10 10"><path d="M5 0 A3.5 3.5 0 0 1 8.5 3.5 C8.5 6 5 10 5 10 C5 10 1.5 6 1.5 3.5 A3.5 3.5 0 0 1 5 0 Z"/></svg>58 Harwick Lane, Sydney NSW 2000</li>
    </ul>
  </section>

</main>
</body>
</html>
```